Dog themed post card for homeowners that may be willing to sell their house.

We will be sending these postcards to homeowners that may be interested in selling their house. Our business is themed around our dog "Wexley"- Wexley Buys Houses. We are using her as the focal point of the business because typically these homeowners get lots of mailers that are similar and we would like stand out with an inviting puppy dog.
We would like to included the icon for facebook and instragam with her handle "@WexleyBuysHouses" and her website WexleyBuysHouses.example and our phone number 555-814-2760.
We will be sending these postcards in batches to various subdivisions. For that reason please consider a format that can easily change the name of the subdivision. We are including the subdivision name because we want the postcard to be slightly more personal/targeted.
Our business is just starting and we would like to get some brand recognition going. We envision Wexley Buys Houses predominately displayed somehow.
I have attached numerous pictures of Wexley. We envision using one on each side of the postcard. Below are phrases we would like to include on the postcard in a format that you see fitting. Please use the verbiage below and not what is sketched on the uploaded postcard. The below verbiage is the most up to date.
-I recently bought a house in (subdivision name) and would love to buy yours.
-Call my humans today so we can give you a no obligation offer
-No money out of your pocket
-Quick closing
-Any condition
-Can help with moving expenses

Target Market(s)

Home owners with equity in their house that may need to sell quickly. These are generally people that do not enjoy the buying/selling of real estate. It can sometimes be someone who has recently inherited a home and doesnt want to deal with the headache. Other times it may be someone going through a divorce or forclosure and want to sell their home quickly.

Industry/Entity Type

Direct Marketing

Requirements
Must have
• Happy and bright feel. This industry is saturated with less than ethical people and we are trying to convey a very clean, honest, straight forward and scam-free process.

```html
<!DOCTYPE html>
<html lang="en">
<head>
<meta charset="utf-8">
<title>Wexley Buys Houses – Postcard</title>
<link href="https://fonts.googleapis.com/css2?family=Montserrat:wght@500;600;700;800;900&display=swap" rel="stylesheet">
<style>
:root{
  --page:#8a8c8e;
  --navy:#30324a;
  --red:#e2302c;
  --yellow:#f8c51c;
  --sand-light:#efe2d3;
  --sand:#d9c2aa;
  --sand-dark:#b59a80;
  --white:#ffffff;
  --fur-light:#e8e6ea;
  --fur:#a9abbd;
}
*{box-sizing:border-box;margin:0;padding:0}
html,body{width:891px;height:1200px;overflow:hidden;background:var(--page);font-family:"Montserrat",sans-serif}
.postcard{position:absolute;left:61px;width:770px;height:514px;overflow:hidden;background:linear-gradient(120deg,var(--sand-light),var(--sand) 60%,var(--sand-dark))}
.postcard--front{top:58px}
.postcard--back{top:621px}
.scene{position:absolute;inset:0;background:linear-gradient(160deg,rgba(255,255,255,.25),rgba(150,120,95,.25))}
.brand{position:absolute;color:var(--red);font-weight:900;text-transform:uppercase;line-height:.9;letter-spacing:-1px}
.postcard--front .brand{left:28px;top:70px;font-size:78px}
.postcard--back .brand{left:24px;top:40px;font-size:48px}
.dog{position:absolute;border-radius:48% 48% 30% 30%;background:radial-gradient(ellipse at 50% 35%,var(--fur-light),var(--fur) 75%)}
.postcard--front .dog{left:560px;top:130px;width:190px;height:370px;z-index:3}
.postcard--back .dog{left:330px;top:34px;width:118px;height:180px;z-index:3}
.bubble{position:absolute;border:2px solid var(--white);border-radius:50%;background:rgba(255,255,255,.12);display:flex;align-items:center;justify-content:center;color:var(--navy);font-weight:900}
.postcard--front .bubble{left:546px;top:28px;width:110px;height:74px;font-size:28px}
.postcard--back .bubble{left:440px;top:24px;width:84px;height:52px;font-size:21px}
.pointer{position:absolute}
.band-red{position:absolute;left:0;width:100%;height:68px;top:384px;background:var(--red)}
.band-navy{position:absolute;left:0;bottom:0;width:100%;height:62px;background:var(--navy)}
.tagline{position:absolute;left:0;width:520px;top:394px;text-align:center;color:var(--white);font-size:19px;font-weight:500;line-height:1.15}
.tagline .subdivision{font-weight:800;font-size:21px;text-transform:uppercase}
.contact{position:absolute;left:29px;top:10px;text-transform:uppercase}
.contact__label{color:var(--yellow);font-weight:800;font-size:16px}
.contact__value{color:var(--white);font-weight:800;font-size:16px}
.divider{position:absolute;left:316px;top:9px;width:1px;height:44px;background:var(--white)}
.phone-icon{position:absolute;left:322px;top:15px}
.call{position:absolute;left:362px;top:6px}
.call__label{color:var(--yellow);font-weight:800;font-size:14px;text-transform:uppercase}
.call__number{color:var(--white);font-weight:900;font-size:28px;line-height:1}
.pitch{position:absolute;left:43px;top:205px;color:var(--navy)}
.pitch__head{font-weight:900;font-size:22px;text-transform:uppercase}
.pitch__body{font-weight:600;font-size:19px;line-height:1.1;width:290px}
.benefits{position:absolute;left:45px;top:290px;list-style:none;color:var(--navy);font-size:16px;font-weight:600}
.benefits li{display:flex;align-items:center;gap:8px;height:21.5px}
.stamp{position:absolute;left:614px;top:33px;width:117px;height:117px;border-radius:14px;background:var(--white)}
.address-line{position:absolute;left:424px;width:310px;height:41px;border-radius:21px;background:var(--white)}
.social{position:absolute;left:30px;top:404px;display:flex;align-items:center;gap:10px;color:var(--white);font-weight:800;font-size:20px}
.social__mark{width:30px;height:30px;border-radius:4px;background:var(--yellow)}
</style>
</head>
<body>

<section class="postcard postcard--front">
  <div class="scene" role="img" aria-label="Sepia photo of a brick house with garage and front walkway"></div>
  <div class="brand">Wexley<br>Buys<br>Houses</div>
  <svg class="pointer" style="left:455px;top:150px" width="120" height="50" viewBox="0 0 120 50"><path d="M4 8 Q50 40 110 38" fill="none" stroke="#fff" stroke-width="3"/><path d="M100 30 L112 38 L100 46" fill="none" stroke="#fff" stroke-width="3"/></svg>
  <div class="bubble">HI!</div>
  <div class="band-red"></div>
  <p class="tagline">I recently bought a house in <span class="subdivision">Maple Hollow</span><br>and would love to buy yours.</p>
  <div class="band-navy">
    <div class="contact"><div class="contact__label">For details visit</div><div class="contact__value">wexley-buyshouses.example</div></div>
    <div class="divider"></div>
    <svg class="phone-icon" width="32" height="32" viewBox="0 0 24 24"><path fill="#f8c51c" d="M6.6 10.8a15 15 0 0 0 6.6 6.6l2.2-2.2a1 1 0 0 1 1-.25 11.4 11.4 0 0 0 3.6.6 1 1 0 0 1 1 1V20a1 1 0 0 1-1 1A17 17 0 0 1 3 4a1 1 0 0 1 1-1h3.5a1 1 0 0 1 1 1c0 1.25.2 2.45.6 3.6a1 1 0 0 1-.25 1z"/></svg>
    <div class="call"><div class="call__label">Call us at</div><div class="call__number">555-814-2760</div></div>
  </div>
  <div class="dog" role="img" aria-label="Photo of Wexley, a fluffy grey and white sheepdog wearing a striped bandana"></div>
</section>

<section class="postcard postcard--back">
  <div class="scene" role="img" aria-label="Sepia photo of an empty living room with fireplace and windows"></div>
  <div class="brand">Wexley<br>Buys<br>Houses</div>
  <svg class="pointer" style="left:270px;top:70px" width="80" height="36" viewBox="0 0 80 36"><path d="M3 6 Q35 28 72 26" fill="none" stroke="#fff" stroke-width="2.5"/><path d="M64 19 L73 26 L64 33" fill="none" stroke="#fff" stroke-width="2.5"/></svg>
  <div class="bubble">HI!</div>
  <div class="dog" role="img" aria-label="Photo of Wexley the sheepdog sitting in her bandana"></div>
  <div class="stamp"></div>
  <div class="address-line" style="top:181px"></div>
  <div class="address-line" style="top:240px"></div>
  <div class="address-line" style="top:298px"></div>
  <div class="address-line" style="top:356px;z-index:2"></div>
  <div class="pitch">
    <div class="pitch__head">Call my humans today</div>
    <div class="pitch__body">so they can give you a no obligation cash offer</div>
  </div>
  <ul class="benefits">
    <li><svg width="20" height="20" viewBox="0 0 20 20"><circle cx="9" cy="11" r="8" fill="#30324a"/><path d="M5 11 L8.5 14.5 L18 3" fill="none" stroke="#f8c51c" stroke-width="3"/></svg>No money out of your pocket</li>
    <li><svg width="20" height="20" viewBox="0 0 20 20"><circle cx="9" cy="11" r="8" fill="#30324a"/><path d="M5 11 L8.5 14.5 L18 3" fill="none" stroke="#f8c51c" stroke-width="3"/></svg>Quick closing</li>
    <li><svg width="20" height="20" viewBox="0 0 20 20"><circle cx="9" cy="11" r="8" fill="#30324a"/><path d="M5 11 L8.5 14.5 L18 3" fill="none" stroke="#f8c51c" stroke-width="3"/></svg>Any condition</li>
    <li><svg width="20" height="20" viewBox="0 0 20 20"><circle cx="9" cy="11" r="8" fill="#30324a"/><path d="M5 11 L8.5 14.5 L18 3" fill="none" stroke="#f8c51c" stroke-width="3"/></svg>I can help with moving expenses</li>
  </ul>
  <div class="band-red"></div>
  <div class="social"><span class="social__mark"></span>@WexleyBuysHouses</div>
  <div class="band-navy">
    <div class="contact"><div class="contact__label">For details visit</div><div class="contact__value">wexley-buyshouses.example</div></div>
    <div class="divider"></div>
    <svg class="phone-icon" width="32" height="32" viewBox="0 0 24 24"><path fill="#f8c51c" d="M6.6 10.8a15 15 0 0 0 6.6 6.6l2.2-2.2a1 1 0 0 1 1-.25 11.4 11.4 0 0 0 3.6.6 1 1 0 0 1 1 1V20a1 1 0 0 1-1 1A17 17 0 0 1 3 4a1 1 0 0 1 1-1h3.5a1 1 0 0 1 1 1c0 1.25.2 2.45.6 3.6a1 1 0 0 1-.25 1z"/></svg>
    <div class="call"><div class="call__label">Call us at</div><div class="call__number">555-814-2760</div></div>
  </div>
</section>

</body>
</html>
```